Cocktail Reception Invitation - For New Office Location

We are a residential property management, investment, and acquisition company and we have recently moved to a new corporate headquarters. We are hosting an event for current customers/vendors, as well as prospects, to show off the new office and enhance the legitimacy of our brand. The event will be a cocktail reception with heavy appetizers/hors d'oeuvres and a bar. We want the invitation to be professional, clean, and somewhat modern. Would be great if we could have it formatted for both electronic delivery AND print, but print is the priority. Thanks in advance for submitting! Photo of the new building attached - does not have to be on the invitation though.

Target Market(s)

Investors, Property Owners, Contractors

Industry/Entity Type

Real Estate

Requirements
Must have
• Must have placeholders for event date, time, location, RSVP, etc. Date is Thursday November 17th from 4-7:00 PM at 418 W Marlow St, Indianapolis, IN 46208. The invitees are a very professional group of people and the invitation should be classy and clean.
Nice to have
• Our colors are Navy Blue, Orange, and dark gray. Not required if it doesn't look good on the invite but it might be nice. I have included a photo of the new office if it makes sens to have it on the invitation.

```html
<!DOCTYPE html>
<html lang="en">
<head>
<meta charset="utf-8">
<title>Corvane – Cocktail Reception Invitation</title>
<link rel="stylesheet" href="https://fonts.googleapis.com/css2?family=Libre+Baskerville:wght@400;700&display=swap">
<style>
  :root {
    --stage: #262626;
    --navy: #2c2d85;
    --navy-deep: #222366;
    --silver: #b7b9bc;
    --silver-light: #c4c6c9;
    --white: #ffffff;
    --gold-soft: rgba(190, 170, 120, 0.55);
    --serif: "Libre Baskerville", "Bookman Old Style", Georgia, serif;
  }
  * { box-sizing: border-box; margin: 0; padding: 0; }
  html, body {
    width: 1200px;
    height: 900px;
    overflow: hidden;
    background: var(--stage);
    font-family: var(--serif);
    color: var(--white);
  }
  .canvas {
    position: relative;
    width: 1200px;
    height: 900px;
  }
  .card {
    position: absolute;
    left: 240px;
    width: 720px;
    height: 400px;
    box-shadow: 0 10px 30px rgba(0, 0, 0, 0.5);
  }

  /* Cover */
  .card--cover {
    top: 40px;
    background: linear-gradient(135deg, var(--silver-light), var(--silver));
  }
  .cover-frame {
    position: absolute;
    inset: 16px;
    border: 2px solid var(--white);
  }
  .cover-band {
    position: absolute;
    top: 0;
    bottom: 0;
    left: 245px;
    width: 230px;
    background: linear-gradient(160deg, var(--navy), var(--navy-deep));
    display: flex;
    flex-direction: column;
    align-items: center;
    justify-content: center;
    text-align: center;
  }
  .brand-name {
    font-weight: 400;
    letter-spacing: 0.04em;
    line-height: 1;
  }
  .cover-band .brand-name { font-size: 46px; margin-bottom: 14px; }
  .brand-tagline {
    text-transform: uppercase;
    letter-spacing: 0.02em;
    line-height: 1.9;
  }
  .cover-band .brand-tagline { font-size: 11px; }

  /* Invitation */
  .card--invite {
    top: 470px;
    background: linear-gradient(150deg, var(--navy) 0%, #28297a 55%, var(--navy-deep) 100%);
    display: flex;
    flex-direction: column;
    align-items: center;
    padding-top: 30px;
    text-align: center;
  }
  .card--invite .brand-name { font-size: 34px; margin-bottom: 6px; }
  .card--invite .brand-tagline { font-size: 8px; line-height: 1.7; margin-bottom: 10px; }
  .divider {
    display: block;
    width: 300px;
    height: 18px;
    margin: 4px 0 8px;
    background: linear-gradient(90deg, transparent, var(--gold-soft) 30%, var(--gold-soft) 70%, transparent);
    mask: linear-gradient(transparent 40%, #000 45%, #000 55%, transparent 60%);
    -webkit-mask: linear-gradient(transparent 40%, #000 45%, #000 55%, transparent 60%);
  }
  .invite-lead { font-size: 14px; letter-spacing: 0.03em; margin-bottom: 4px; }
  .invite-date { font-size: 28px; letter-spacing: 0.03em; margin-bottom: 8px; }
  .invite-place, .invite-time { font-size: 16px; letter-spacing: 0.03em; margin-bottom: 6px; }
  .invite-rsvp { font-size: 14px; letter-spacing: 0.03em; margin-top: 2px; }
</style>
</head>
<body>
<main class="canvas">
  <section class="card card--cover" aria-label="Invitation cover">
    <div class="cover-frame"></div>
    <div class="cover-band">
      <h1 class="brand-name">Corvane</h1>
      <p class="brand-tagline">Investment | Management<br>(Re)Development</p>
    </div>
  </section>

  <section class="card card--invite" aria-label="Invitation details">
    <h2 class="brand-name">Corvane</h2>
    <p class="brand-tagline">Investment | Management<br>(Re)Development</p>
    <span class="divider" role="img" aria-label="Decorative flourish divider"></span>
    <p class="invite-lead">Please join us for A Special Cocktail Reception</p>
    <p class="invite-date">Thursday, 17th November 2016</p>
    <p class="invite-place">418 W Marlow St, Indianapolis, IN 46208</p>
    <p class="invite-time">starting : 08.00 pm</p>
    <p class="invite-rsvp">RSVP by 15th November 2016</p>
    <span class="divider" role="img" aria-label="Decorative flourish divider"></span>
  </section>
</main>
</body>
</html>
```